Brightwell Amusements Investor Brochure

Start Up Company Brightwell Amusements requires 4 page A4 size brochure outlining and detailing new product. Draft layout attached. Information and points of difference included. Company logo and graphics attached. Final design should sell to investors.

```html
<!DOCTYPE html>
<html lang="en">
<head>
<meta charset="utf-8">
<title>Brightwell Amusements – Investor Brochure</title>
<link href="https://fonts.googleapis.com/css2?family=Roboto+Condensed:wght@300;400;700&display=swap" rel="stylesheet">
<style>
:root{
  --brand:#5b8bd0;
  --brand-dark:#3f66a3;
  --ink:#1c2a44;
  --map-light:#d9e7f7;
  --world:#c4d6ef;
  --white:#ffffff;
  --kiosk:#1d2a45;
}
*{margin:0;padding:0;box-sizing:border-box}
html,body{width:1200px;height:849px;overflow:hidden;background:var(--white)}
body{font-family:"Roboto Condensed",Arial,sans-serif;color:var(--ink)}
.page{position:relative;width:1200px;height:849px;overflow:hidden}
.abs{position:absolute}
.backdrop{left:0;top:0}
.headline{font-weight:300;text-transform:uppercase;line-height:.93;letter-spacing:-.5px}
.headline b{font-weight:700}
.headline--au{left:20px;top:16px;font-size:46px;color:var(--white)}
.headline--global{left:612px;top:20px;font-size:50px;color:var(--brand)}
.au-map{left:40px;top:150px;width:370px;height:305px;background:var(--map-light);border-radius:45% 40% 35% 50%/40% 45% 45% 35%}
.world-map{left:410px;top:115px;width:770px;height:385px;background:var(--world);opacity:.8;border-radius:30% 30% 40% 40%/35% 35% 50% 50%}
.stat{left:40px;top:216px;font-size:18px;font-weight:700;line-height:1.2;color:var(--ink)}
.note{left:40px;top:282px;font-size:11px;line-height:1.2;color:var(--ink)}
.airports{left:22px;top:337px;list-style:none}
.airports li{display:flex;align-items:center;height:25px;font-size:7.5px;text-transform:uppercase;color:var(--ink)}
.airports i{display:block;width:20px;height:17px;margin-right:4px}
.features{left:140px;top:460px;width:265px;list-style:none;color:var(--white);font-size:11px;line-height:14px}
.features li{position:relative;padding-left:13px;margin-bottom:6px}
.features li::before{content:"";position:absolute;left:1px;top:5px;width:5px;height:5px;border-radius:50%;background:var(--white)}
.donut{left:155px;top:595px}
.kiosk{left:368px;top:396px;width:192px;height:444px;z-index:2}
.global-fact{left:612px;top:176px;font-size:34px;font-weight:700;line-height:1.27;color:#4d6f9f}
.headline--wifi{left:612px;top:528px;font-size:45px;font-weight:300;color:var(--brand);letter-spacing:-.5px;white-space:nowrap}
.headline--wifi b{font-weight:700}
.chart{left:690px;top:588px}
.chart text{font-family:"Roboto Condensed",Arial,sans-serif}
</style>
</head>
<body>
<main class="page">
  <svg class="abs backdrop" width="1200" height="849" aria-hidden="true">
    <path d="M0 0 H400 C430 250 530 520 640 640 C700 710 760 790 810 849 H0 Z" fill="var(--brand)"/>
  </svg>

  <h1 class="abs headline headline--au">Coming soon<br>to <b>airports</b><br>across Australia</h1>
  <div class="abs au-map" role="img" aria-label="Map of Australia with kiosk markers at airports"></div>

  <p class="abs stat">145,000,000+ Passenger Movements<br>for YE Feb 2014. Up 3.1% on 2013.</p>
  <p class="abs note">New Airport announced for<br>Western Sydney to cope with<br>increased demand.</p>

  <ul class="abs airports">
    <li><i style="background:#eef5fd"></i>Sydney 38,437,737</li>
    <li><i style="background:#e6f0fc"></i>Melbourne 30,484,074</li>
    <li><i style="background:#dcebfb"></i>Brisbane 21,570,625</li>
    <li><i style="background:#d2e6fa"></i>Perth 12,989,955</li>
    <li><i style="background:#c8e1f9"></i>Adelaide 7,460,471</li>
    <li><i style="background:#bedcf8"></i>Gold Coast 5,789,986</li>
    <li><i style="background:#b3d7f7"></i>Cairns 4,293,485</li>
    <li><i style="background:#a8d2f6"></i>Canberra 2,931,006</li>
    <li><i style="background:#9dccf5"></i>Hobart 2,098,416</li>
    <li><i style="background:#92c7f4"></i>Darwin 2,023,665</li>
    <li><i style="background:#86c2f3"></i>Townsville 1,543,457</li>
    <li><i style="background:#7bbdf2"></i>Launceston 1,267,589</li>
    <li><i style="background:#70b8f1"></i>Williamtown 1,208,188</li>
    <li><i style="background:#65b3f0"></i>Mackay 1,083,805</li>
    <li><i style="background:#59aeef"></i>Sunshine Coast 891,300</li>
    <li><i style="background:#4ea9ee"></i>Karratha 763,137</li>
    <li><i style="background:#43a5ed"></i>Rockhampton 649,368</li>
    <li><i style="background:#38a0ec"></i>Alice Springs 667,383</li>
    <li><i style="background:#2d9beb"></i>Gladstone 500,429</li>
    <li><i style="background:#2296ea"></i>Port Hedland 491,274</li>
  </ul>

  <ul class="abs features">
    <li>Current technology allows up to 10,000 encrypted<br>digital movies to be stored on a kiosk.</li>
    <li>Multiple customers can simultaneously browse<br>and rent movies on the Kiosks FREE Wifi.</li>
    <li>Travellers are always looking to be entertained<br>when flying ... the perfect time to watch a movie!</li>
    <li>Target of 1 million transactions in the first 12 months.</li>
  </ul>

  <svg class="abs donut" width="230" height="230" viewBox="0 0 230 230" role="img" aria-label="Donut chart of passenger movements by airport">
    <g transform="rotate(-90 115 115)" fill="none" stroke-width="48">
      <circle cx="115" cy="115" r="89" pathLength="137.2" stroke="#eef5fd" stroke-dasharray="38.4 137.2" stroke-dashoffset="0"/>
      <circle cx="115" cy="115" r="89" pathLength="137.2" stroke="#e6f0fc" stroke-dasharray="30.5 137.2" stroke-dashoffset="-38.4"/>
      <circle cx="115" cy="115" r="89" pathLength="137.2" stroke="#dcebfb" stroke-dasharray="21.6 137.2" stroke-dashoffset="-68.9"/>
      <circle cx="115" cy="115" r="89" pathLength="137.2" stroke="#d2e6fa" stroke-dasharray="13 137.2" stroke-dashoffset="-90.5"/>
      <circle cx="115" cy="115" r="89" pathLength="137.2" stroke="#c8e1f9" stroke-dasharray="7.5 137.2" stroke-dashoffset="-103.5"/>
      <circle cx="115" cy="115" r="89" pathLength="137.2" stroke="#bedcf8" stroke-dasharray="5.8 137.2" stroke-dashoffset="-111"/>
      <circle cx="115" cy="115" r="89" pathLength="137.2" stroke="#b3d7f7" stroke-dasharray="4.3 137.2" stroke-dashoffset="-116.8"/>
      <circle cx="115" cy="115" r="89" pathLength="137.2" stroke="#a8d2f6" stroke-dasharray="2.9 137.2" stroke-dashoffset="-121.1"/>
      <circle cx="115" cy="115" r="89" pathLength="137.2" stroke="#9dccf5" stroke-dasharray="2.1 137.2" stroke-dashoffset="-124"/>
      <circle cx="115" cy="115" r="89" pathLength="137.2" stroke="#92c7f4" stroke-dasharray="2 137.2" stroke-dashoffset="-126.1"/>
      <circle cx="115" cy="115" r="89" pathLength="137.2" stroke="#86c2f3" stroke-dasharray="1.5 137.2" stroke-dashoffset="-128.1"/>
      <circle cx="115" cy="115" r="89" pathLength="137.2" stroke="#7bbdf2" stroke-dasharray="1.3 137.2" stroke-dashoffset="-129.6"/>
      <circle cx="115" cy="115" r="89" pathLength="137.2" stroke="#70b8f1" stroke-dasharray="1.2 137.2" stroke-dashoffset="-130.9"/>
      <circle cx="115" cy="115" r="89" pathLength="137.2" stroke="#65b3f0" stroke-dasharray="1.1 137.2" stroke-dashoffset="-132.1"/>
      <circle cx="115" cy="115" r="89" pathLength="137.2" stroke="#59aeef" stroke-dasharray="0.9 137.2" stroke-dashoffset="-133.2"/>
      <circle cx="115" cy="115" r="89" pathLength="137.2" stroke="#4ea9ee" stroke-dasharray="0.8 137.2" stroke-dashoffset="-134.1"/>
      <circle cx="115" cy="115" r="89" pathLength="137.2" stroke="#43a5ed" stroke-dasharray="0.6 137.2" stroke-dashoffset="-134.9"/>
      <circle cx="115" cy="115" r="89" pathLength="137.2" stroke="#38a0ec" stroke-dasharray="0.7 137.2" stroke-dashoffset="-135.5"/>
      <circle cx="115" cy="115" r="89" pathLength="137.2" stroke="#2d9beb" stroke-dasharray="0.5 137.2" stroke-dashoffset="-136.2"/>
      <circle cx="115" cy="115" r="89" pathLength="137.2" stroke="#2296ea" stroke-dasharray="0.5 137.2" stroke-dashoffset="-136.7"/>
    </g>
  </svg>

  <h2 class="abs headline headline--global">Technology built for<br><b>global</b> expansion</h2>
  <div class="abs world-map" role="img" aria-label="Striped world map"></div>
  <p class="abs global-fact">Top 20 Airports in<br>the world exceeded<br>1.2 billion passengers<br>in 2013.</p>

  <svg class="abs kiosk" width="192" height="444" viewBox="0 0 192 444" role="img" aria-label="Brightwell Amusements movie kiosk with Movies for Travellers display">
    <defs>
      <linearGradient id="kiosk-fill" x1="0" y1="0" x2="0" y2="1">
        <stop offset="0" stop-color="#2e3f63"/>
        <stop offset="1" stop-color="var(--kiosk)"/>
      </linearGradient>
    </defs>
    <path d="M52 0 H150 C160 120 170 260 168 400 L188 412 V444 H0 V412 L20 400 C40 260 48 120 52 0 Z" fill="url(#kiosk-fill)"/>
  </svg>

  <h2 class="abs headline--wifi">Incorporating Blazing <b>Fast</b> Wifi</h2>

  <svg class="abs chart" width="480" height="195" viewBox="0 0 480 195" role="img" aria-label="Bar chart of connection speeds in Mbps">
    <g font-size="11" fill="var(--ink)" text-anchor="end">
      <text x="95" y="16">UltraLink 802.11ad</text>
      <text x="95" y="37">Wifi 802.11ac</text>
      <text x="95" y="58">Wifi 802.11n</text>
      <text x="95" y="79">QBN 100</text>
      <text x="95" y="100">QBN 50</text>
      <text x="95" y="121">QBN 25</text>
      <text x="95" y="142">QBN 12</text>
      <text x="95" y="163">ADSL 2+</text>
    </g>
    <g fill="var(--brand)" stroke="var(--brand-dark)" stroke-width=".8">
      <rect x="100" y="4" width="281" height="14"/>
      <rect x="100" y="25" width="52" height="14"/>
      <rect x="100" y="46" width="12" height="14"/>
      <rect x="100" y="67" width="4" height="14"/>
      <rect x="100" y="88" width="2" height="14"/>
      <rect x="100" y="109" width="1" height="14"/>
      <rect x="100" y="130" width="1" height="14"/>
      <rect x="100" y="151" width="1" height="14"/>
    </g>
    <g font-size="9">
      <text x="377" y="15" fill="var(--white)" text-anchor="end">Future Devices to Download SD Movies in a few seconds</text>
      <text x="380" y="36" fill="var(--ink)" text-anchor="end">Nova Phone X4 &amp; X5</text>
      <text x="380" y="57" fill="var(--ink)" text-anchor="end">2013 Model Nova Tablet - Download SD Movies in Under 3 Minutes</text>
    </g>
    <line x1="100" y1="0" x2="100" y2="170" stroke="var(--ink)" stroke-width=".8"/>
    <line x1="100" y1="170" x2="421" y2="170" stroke="var(--ink)" stroke-width=".8"/>
    <g font-size="11" fill="var(--ink)" text-anchor="middle">
      <text x="100" y="184">0</text><text x="140" y="184">1000</text><text x="180" y="184">2000</text>
      <text x="220" y="184">3000</text><text x="260" y="184">4000</text><text x="301" y="184">5000</text>
      <text x="341" y="184">6000</text><text x="381" y="184">7000</text><text x="421" y="184">8000</text>
      <text x="450" y="184">Mbps</text>
    </g>
  </svg>
</main>
</body>
</html>
```